Landing Page IT Security Vendor

We need a landing page that uses our colour scheme (www.brantowguard.example). We created a draft (see attached). We do not need standard stock template design pages. Please only apply if you can design pages from scratch and try to be as close as possible to our draft. It is ok to also purchase commecrial stock pictures

Coding

Coded - Design and coding required

Number of Pages Required

1 page

```html
<!DOCTYPE html>
<html lang="en">
<head>
<meta charset="utf-8">
<title>Brantow Guard – Security Awareness Training</title>
<link href="https://fonts.googleapis.com/css2?family=Questrial&family=Mulish:wght@400;600;700&display=swap" rel="stylesheet">
<style>
:root{
  --teal:#00b6c1;
  --teal-dark:#009aa4;
  --orange:#f9a61c;
  --white:#ffffff;
  --paper:#f7f7f7;
  --ink:#2d2d2d;
  --body:#555555;
  --band:#6c6c6c;
  --photo-a:#2f3b44;
  --photo-b:#c9a88f;
}
*{box-sizing:border-box;margin:0;padding:0}
html,body{width:750px;height:1200px;overflow:hidden}
body{position:relative;background:var(--paper);font-family:'Mulish',sans-serif;color:var(--ink)}
.abs{position:absolute}
.display{font-family:'Questrial',sans-serif}

.hero{left:0;top:0;width:750px;height:395px;background:var(--teal)}
.brand{left:35px;top:20px;display:flex;align-items:center;gap:6px;color:var(--white);font-family:'Questrial',sans-serif;font-size:20px}
.brand-dot{width:14px;height:14px;border-radius:50%;background:var(--orange)}
.award{top:31px;display:flex;gap:7px;align-items:center;color:var(--white);font-size:6.8px;line-height:8.4px}
.award svg{flex:none}
.tagline{left:55px;top:116px;color:var(--white);font-size:11px;letter-spacing:.3px;font-weight:600}
.headline{left:55px;top:134px;width:320px;color:var(--white);font-size:21px;line-height:28.6px;letter-spacing:.1px;white-space:nowrap}
.btn-ghost{left:385px;top:164px;width:96px;height:20px;border-radius:10px;background:var(--white);color:#555;font-size:8.5px;display:flex;align-items:center;justify-content:center;z-index:2}
.photo{left:470px;top:75px;width:240px;height:265px;border-radius:110px 110px 0 0;background:linear-gradient(180deg,var(--photo-b) 0%,#e9e4df 45%,var(--photo-a) 100%);opacity:.9}
.help{left:0;width:750px;top:294px;text-align:center;color:var(--white);font-size:11px;font-weight:700;letter-spacing:.4px}
.dash{left:210px;top:318px}

.panel{left:35px;top:340px;width:680px;height:265px;background:var(--paper)}
.card{top:360px;width:200px;height:200px;background:var(--white);padding:14px 15px}
.card h3{color:var(--orange);font-size:9.2px;line-height:11px;font-weight:600;text-transform:uppercase;margin-bottom:11px}
.card .lead{font-size:8px;line-height:11px;font-weight:600;color:var(--ink);margin-bottom:11px}
.card .copy{font-size:7.2px;line-height:11px;color:var(--body)}
.card .btn{position:absolute;left:15px;bottom:18px;width:170px;height:20px}
.btn{border-radius:10px;background:var(--orange);color:var(--white);font-size:8.5px;display:flex;align-items:center;justify-content:center}
.btn.teal{background:var(--teal)}

.band{left:0;top:610px;width:750px;height:75px;background:linear-gradient(115deg,#6a6a6a,#7a7a7a 40%,#616161 70%,#747474)}
.band-text{left:129px;top:636px;color:var(--white);font-size:18.5px;font-weight:600;letter-spacing:.2px}
.band-btn{left:540px;top:638px;width:80px;height:20px}

.trust-title{left:55px;top:730px;width:310px;font-size:18.5px;line-height:24px;color:#333;white-space:nowrap}
.trust-copy{left:55px;top:812px;width:300px;font-size:7.3px;line-height:11px;color:var(--body)}
.trust-copy p{margin-bottom:11px}
.trust-btn{left:55px;top:905px;width:200px;height:20px}
.clients{left:385px;top:740px;width:310px;height:165px;display:grid;grid-template-columns:repeat(4,1fr);grid-template-rows:repeat(3,1fr);gap:10px;align-items:center}
.client{font-family:'Questrial',sans-serif;font-size:12px;color:#1f3d7a;text-align:center}
.client.wide{grid-column:span 2;font-size:15px}

.footer{left:0;top:975px;width:750px;height:225px;background:var(--teal);color:var(--white)}
.f-head{top:1010px;font-size:9.5px;font-weight:600;letter-spacing:.3px;color:var(--white)}
.f-col{top:1031px;font-size:7.6px;line-height:12px;color:var(--white)}
.f-rule{left:55px;top:1114px;width:640px;height:1px;background:rgba(255,255,255,.6)}
.f-brand{left:58px;top:1142px;font-family:'Questrial',sans-serif;font-size:14px;color:var(--white)}
.f-rights{left:55px;top:1166px;font-size:7.4px;color:var(--white)}
.badges{left:168px;top:1135px;width:527px;height:40px;display:flex;justify-content:space-between;align-items:center}
.badge{background:rgba(255,255,255,.85)}
</style>
</head>
<body>

<section class="abs hero" aria-label="Hero"></section>
<div class="abs photo" role="img" aria-label="Photo of a smiling professional woman in a dark blazer holding an open laptop"></div>

<div class="abs brand"><span class="brand-dot"></span><span>Brantow</span></div>

<div class="abs award" style="left:168px">
  <svg width="14" height="14" viewBox="0 0 14 14"><path d="M3 1h8v3a4 4 0 0 1-8 0zM1 2h2v2a2 2 0 0 1-2-2zM11 2h2a2 2 0 0 1-2 2zM6 8h2v3h2v2H4v-2h2z" fill="#fff"/></svg>
  <span>In 2020, BRANTOW won the SecureTech<br>Excellence Award for Best "Anti Phishing</span>
</div>
<div class="abs award" style="left:338px">
  <svg width="18" height="14" viewBox="0 0 18 14"><circle cx="9" cy="7" r="5.5" fill="none" stroke="#fff" stroke-width="1.2"/><path d="M9 4l1 2h2l-1.6 1.3.6 2.2L9 8.3 7 9.5l.6-2.2L6 6h2z" fill="#fff"/></svg>
  <span>In 2020, BRANTOW won the SecureTech Excellence<br>Award for Best "Security Education Platform</span>
</div>
<div class="abs award" style="left:540px">
  <svg width="16" height="16" viewBox="0 0 16 16"><circle cx="8" cy="8" r="6.5" fill="none" stroke="#fff" stroke-width="1.2"/><text x="8" y="11" font-size="8" text-anchor="middle" fill="#fff" font-family="sans-serif">1</text></svg>
  <span>2020 Gold Winner "Cyber Security Education<br>and Training In the Defense Product Review</span>
</div>

<div class="abs tagline">CYBER SECURITY STARTS WITH PEOPLE</div>
<h1 class="abs headline display" style="font-weight:400">TRAIN YOUR STAFF<br>WITH BRANTOW AND IMPROVE<br>CYBER&nbsp; SECURITY<br>AWARENESS</h1>
<div class="abs btn-ghost">Request a demo</div>

<div class="abs help">HOW CAN WE HELP?</div>
<svg class="abs dash" width="332" height="24" viewBox="0 0 332 24">
  <g stroke="#fff" stroke-width="0.8" stroke-dasharray="3 2" fill="none">
    <path d="M0 1H332"/><path d="M10 1V24"/><path d="M165 1V24"/><path d="M320 1V24"/>
  </g>
</svg>

<div class="abs panel"></div>

<article class="abs card" style="left:55px">
  <h3>Import our training courses<br>in your LMS</h3>
  <p class="lead">Buy out of the box or custom tailored security courses you can import in your elearning (SCORM)</p>
  <p class="copy">BRANTOW offers 250 fully customizable training modules in +30 languages. Games, videos, exams, posters, offline, micro-training and much more!</p>
  <div class="btn">Explore our training</div>
</article>
<article class="abs card" style="left:275px">
  <h3>Let us develop a security<br>awareness&nbsp; program</h3>
  <p class="lead">BRANTOW Security will assist you in improving security awareness - with money back guarantee!</p>
  <p class="copy">Our security awareness specialists will identify risky users via phishing simulations. We develop a tailored awareness program and reduce your exposure to social hacking.</p>
  <div class="btn teal">Explore our services</div>
</article>
<article class="abs card" style="left:495px">
  <h3>Install the Brantow software on-premise or get access to the SaaS version</h3>
  <p class="lead">You want to run the campaign yourself? Choose your prefered setup type and get started in 24h!</p>
  <p class="copy">The BRANTOW software can be installed on-premise or in the cloud. If you don't want to deal with the installation we onboard you in 24 h on our SaaS!</p>
  <div class="btn">Explore our software</div>
</article>

<section class="abs band" aria-label="MSSP"></section>
<div class="abs band-text">BRANTOW is also available for MSSP</div>
<div class="abs btn band-btn">Learn more</div>

<h2 class="abs trust-title display" style="font-weight:400">Already over 12'000'000<br>Employees worldwide trust and<br>use BRANTOW.</h2>
<div class="abs trust-copy">
  <p>Brantow Guard is a name you can trust! Because we have won countless awards since 2015 and help well-known brands around the world.</p>
  <p>You know you're getting a quality solution with us.</p>
  <p>Our services can be customized to fit your needs and company size. Talk to our team today to learn more.</p>
</div>
<div class="abs btn trust-btn">Get in contact with the brantow team now!</div>

<div class="abs clients" aria-label="Client names">
  <div class="client">Norvalis</div>
  <div class="client" style="color:#c8102e">Railtek</div>
  <div class="client" style="color:#c8102e">Hausfort</div>
  <div class="client" style="color:#c8102e">Kellmann</div>
  <div class="client wide">Alpenflug</div>
  <div class="client wide" style="color:#00928f">Ravenmill</div>
  <div class="client">Stellwerk Data</div>
  <div class="client wide" style="color:#111">Chemora</div>
  <div class="client" style="color:#f26b1d">Urbaclean</div>
</div>

<footer class="abs footer"></footer>
<div class="abs f-head" style="left:55px">CONTACTS</div>
<div class="abs f-head" style="left:550px">LANGUAGE</div>
<div class="abs f-col" style="left:55px">Address: Europe Brantow Guard<br>AG Seestrasse 18 | 6003<br>Lucerne | Switzerland</div>
<div class="abs f-col" style="left:220px">Address: North America Brantow Guard<br>USA 4410 Meadow Park Dr Suite 210<br>Denver, CO 80216</div>
<div class="abs f-col" style="left:385px">Phone Global: +41 55 010 20 30<br>Phone USA: +1-555-010-2200<br>Phone USA Support: +1-555-010-2201<br>Phone France: +33 600 010 200<br>Phone UK: +44 (0) 7700 900123</div>
<div class="abs f-col" style="left:550px">English &nbsp;<svg width="7" height="5" viewBox="0 0 7 5"><path d="M1 1l2.5 2.5L6 1" stroke="#fff" fill="none"/></svg></div>
<div class="abs f-rule"></div>
<div class="abs f-brand">Brantow</div>
<div class="abs f-rights">All Rights Reserved 2020</div>
<div class="abs badges" aria-label="Awards and certifications">
  <div class="badge" style="width:40px;height:40px;border-radius:4px"></div>
  <div class="badge" style="width:42px;height:42px;border-radius:50%"></div>
  <div class="badge" style="width:32px;height:42px;border-radius:4px"></div>
  <div class="badge" style="width:36px;height:42px"></div>
  <div class="badge" style="width:34px;height:42px"></div>
  <div class="badge" style="width:32px;height:42px"></div>
  <div class="badge" style="width:56px;height:24px;border-radius:4px"></div>
  <div class="badge" style="width:34px;height:34px;border-radius:4px"></div>
  <div class="badge" style="width:64px;height:26px;border-radius:13px"></div>
  <div class="badge" style="width:34px;height:34px;border-radius:50%"></div>
</div>

</body>
</html>
```